Korvane blockchain

A Blockchain investment company template for a switzerland based company. The company is also offering its own blockchain infrastructure in partnership with a top 200 blockchain project, on which blockchain startups can develop their ideas.
In addition, co-working spaces are offered in an innovation center.
So these three parts should be covered in the template

1. Crypto investment
2. Offering the blockchain infrastructure
3. Co-working spaces (https://travelnix.example/)

Target Market(s)

Blockchain / Crypto

Colors
ec1f27

Requirements
Must have
• Connection to the three parts mentioned in the description
inculding to logo attached
Nice to have
• connection to switzerland

```html
<!DOCTYPE html>
<html lang="en">
<head>
<meta charset="utf-8">
<title>Korvane Blockchain – Presentation Template</title>
<link rel="stylesheet" href="https://fonts.googleapis.com/css2?family=Roboto:wght@700;900&family=Lato:wght@400&display=swap">
<style>
  :root {
    --brand-red: #ec1f27;
    --ink: #111111;
    --body-text: #3a3a3a;
    --paper: #ffffff;
    --stage: #8e8e8e;
    --navy-deep: #0a1440;
    --navy-bright: #1d3ab8;
    --mist: #dfe7ee;
  }
  * { box-sizing: border-box; margin: 0; padding: 0; }
  html, body { width: 1200px; height: 1042px; overflow: hidden; }
  body { background: var(--stage); position: relative; font-family: "Lato", sans-serif; }

  .slide {
    position: absolute;
    width: 536px;
    height: 301px;
    overflow: hidden;
    background: var(--paper);
    box-shadow: 0 2px 8px rgba(0,0,0,0.25);
  }
  .col-left  { left: 51px; }
  .col-right { left: 613px; }
  .row-1 { top: 42px; }
  .row-2 { top: 370px; }
  .row-3 { top: 699px; }

  .red-band { position: absolute; top: 0; height: 100%; width: 161px; background: var(--brand-red); }
  .photo { position: absolute; top: 23px; width: 161px; height: 254px; }

  .title {
    position: absolute;
    font-family: "Roboto", sans-serif;
    font-weight: 900;
    font-size: 47px;
    line-height: 46px;
    letter-spacing: -0.5px;
    color: var(--ink);
  }
  .title .accent { color: var(--brand-red); display: block; }
  .title .main { display: block; }

  .body-copy {
    position: absolute;
    top: 124px;
    width: 286px;
    font-size: 12.6px;
    line-height: 21.3px;
    color: var(--body-text);
  }

  .wordmark {
    position: absolute;
    font-family: "Roboto", sans-serif;
    font-weight: 700;
    font-size: 5.6px;
    color: var(--ink);
    white-space: nowrap;
    transform: translateX(-50%);
  }

  /* Cover */
  .cover-bg {
    position: absolute; inset: 0;
    background:
      radial-gradient(ellipse 70% 45% at 50% 100%, #6f9de8 0%, #2a4fc4 35%, rgba(29,58,184,0) 75%),
      linear-gradient(180deg, var(--navy-deep) 0%, #15268a 55%, var(--navy-bright) 100%);
  }
  .cover-name {
    position: absolute; left: 50%; top: 116px;
    transform: translateX(-50%);
    font-family: "Roboto", sans-serif; font-weight: 700;
    font-size: 28px; letter-spacing: -0.8px;
    color: var(--paper); white-space: nowrap;
  }

  /* Agenda */
  .agenda-bg {
    position: absolute; inset: 0;
    background: linear-gradient(120deg, #cfd6dc 0%, var(--mist) 45%, #e9eef2 100%);
  }
  .agenda-title { left: 22px; top: 47px; font-size: 45px; }
  .agenda-list { position: absolute; left: 21px; top: 117px; list-style: none; }
  .agenda-list li {
    display: flex; align-items: center;
    height: 28.6px;
    font-size: 14.6px; color: #2d2d2d;
  }
  .agenda-list svg { width: 12px; height: 12px; margin-right: 16px; flex: none; }

  /* Thank you */
  .thanks-bg {
    position: absolute; inset: 0;
    background:
      linear-gradient(180deg, #3a0a0c 0%, #b3141b 30%, #7a0d12 52%, #d81a22 62%, #5a0a0e 100%);
  }
  .thanks-text {
    position: absolute; left: 0; width: 100%; top: 104px;
    text-align: center;
    font-family: "Roboto", sans-serif; font-weight: 900;
    font-size: 80px; line-height: 90px; letter-spacing: -1px;
    color: var(--paper);
  }
</style>
</head>
<body>

  <!-- Cover -->
  <section class="slide col-left row-1 cover">
    <div class="cover-bg" role="img" aria-label="Deep blue background with a glowing network globe of connected points"></div>
    <p class="cover-name">Korvane Blockchain</p>
  </section>

  <!-- Blockchain infrastructure -->
  <section class="slide col-right row-1">
    <div class="red-band" style="left:0"></div>
    <div class="photo" style="left:41px;background:linear-gradient(160deg,#1b3c78 0%,#0f2452 55%,#08132e 100%)" role="img" aria-label="Engineers working at monitors in a blue-lit server room"></div>
    <h2 class="title" style="left:236px;top:20px"><span class="accent">Blockchain</span><span class="main">Infrastructure</span></h2>
    <p class="body-copy" style="left:237px">Lorem ipsum dolor sit amet, consectetur adipiscing elit, sed do eiusmod tempor incididunt ut labore et dolore magna ipsum suspendisse ultrices gravida. Risus comecenas accumsan lacus vel facilisis. Lorem ipsum dolor sit amet, consectetur adipiscing elit, sed do eiusmod tempor incididunt ut labore et dolore magna ipsum suspendisse ultrices gravida</p>
    <span class="wordmark" style="left:499px;top:285px">Korvane Blockchain</span>
  </section>

  <!-- Agenda -->
  <section class="slide col-left row-2">
    <div class="agenda-bg" role="img" aria-label="Faded photo of hands with a calculator over financial charts"></div>
    <h2 class="title agenda-title">Agenda</h2>
    <ul class="agenda-list">
      <li><svg viewBox="0 0 12 12" aria-hidden="true"><circle cx="6" cy="6" r="5" fill="none" stroke="#ec1f27" stroke-width="1.6"/><path d="M3.6 6.1 5.3 7.7 8.4 4.4" fill="none" stroke="#ec1f27" stroke-width="1.6"/></svg>Introduction</li>
      <li><svg viewBox="0 0 12 12" aria-hidden="true"><circle cx="6" cy="6" r="5" fill="none" stroke="#ec1f27" stroke-width="1.6"/><path d="M3.6 6.1 5.3 7.7 8.4 4.4" fill="none" stroke="#ec1f27" stroke-width="1.6"/></svg>Crypto investment</li>
      <li><svg viewBox="0 0 12 12" aria-hidden="true"><circle cx="6" cy="6" r="5" fill="none" stroke="#ec1f27" stroke-width="1.6"/><path d="M3.6 6.1 5.3 7.7 8.4 4.4" fill="none" stroke="#ec1f27" stroke-width="1.6"/></svg>Offering the blockchain infrastructure</li>
      <li><svg viewBox="0 0 12 12" aria-hidden="true"><circle cx="6" cy="6" r="5" fill="none" stroke="#ec1f27" stroke-width="1.6"/><path d="M3.6 6.1 5.3 7.7 8.4 4.4" fill="none" stroke="#ec1f27" stroke-width="1.6"/></svg>Co-working spaces</li>
      <li><svg viewBox="0 0 12 12" aria-hidden="true"><circle cx="6" cy="6" r="5" fill="none" stroke="#ec1f27" stroke-width="1.6"/><path d="M3.6 6.1 5.3 7.7 8.4 4.4" fill="none" stroke="#ec1f27" stroke-width="1.6"/></svg>Thank you</li>
    </ul>
    <span class="wordmark" style="left:499px;top:287px">Korvane Blockchain</span>
  </section>

  <!-- Co-working spaces -->
  <section class="slide col-right row-2">
    <div class="red-band" style="left:375px"></div>
    <div class="photo" style="left:334px;background:linear-gradient(170deg,#e8e6e2 0%,#c9c2b8 50%,#8d7e72 100%)" role="img" aria-label="Colleagues chatting in a bright shared office"></div>
    <h2 class="title" style="left:30px;top:20px"><span class="accent">Co-working</span><span class="main">Spaces</span></h2>
    <p class="body-copy" style="left:30px">Lorem ipsum dolor sit amet, consectetur adipiscing elit, sed do eiusmod tempor incididunt ut labore et dolore magna ipsum suspendisse ultrices gravida. Risus comecenas accumsan lacus vel facilisis. Lorem ipsum dolor sit amet, consectetur adipiscing elit, sed do eiusmod tempor incididunt ut labore et dolore magna ipsum suspendisse ultrices gravida</p>
    <span class="wordmark" style="left:298px;top:287px">Korvane Blockchain</span>
  </section>

  <!-- Crypto investment -->
  <section class="slide col-left row-3">
    <div class="red-band" style="left:375px"></div>
    <div class="photo" style="left:334px;background:radial-gradient(ellipse 60% 40% at 50% 62%,#3f78e0 0%,#1a2f6a 45%,#0b0f1e 100%)" role="img" aria-label="Finger touching a glowing digital coin between gold coins"></div>
    <h2 class="title" style="left:30px;top:20px"><span class="accent">Crypto</span><span class="main">Investment</span></h2>
    <p class="body-copy" style="left:30px">Lorem ipsum dolor sit amet, consectetur adipiscing elit, sed do eiusmod tempor incididunt ut labore et dolore magna ipsum suspendisse ultrices gravida. Risus comecenas accumsan lacus vel facilisis. Lorem ipsum dolor sit amet, consectetur adipiscing elit, sed do eiusmod tempor incididunt ut labore et dolore magna ipsum suspendisse ultrices gravida</p>
    <span class="wordmark" style="left:298px;top:287px">Korvane Blockchain</span>
  </section>

  <!-- Thank you -->
  <section class="slide col-right row-3">
    <div class="thanks-bg" role="img" aria-label="Red-toned Swiss alpine peaks reflected in a mountain lake"></div>
    <p class="thanks-text">Thank You</p>
    <span class="wordmark" style="left:486px;top:275px;font-size:9.5px;color:#ffffff">Korvane Blockchain</span>
  </section>

</body>
</html>
```